Gordon Pellbrook Consulting - Web Design Project

We need a web design for my new edgy consulting business specializing in innovation, technology and strategy.

It is our personal goal to turn each client into raving fans by helping them achieve their own business goals and aspirations through assisting them in raising their own innovation and marketing standards.

We provide our personalised and state-of-the-art services to our clients and boards who represent some of the world greatest innovative thinkers.
Updates

Here is some other information which may help shape your thinking.

I've had direct Involvement in the development of the following iPad, iPhone Applications and websites

FarbeyondOzlands.com (TerraLink platform) by Voyage Bureau
http://farbeyondozlands.example.au

Sail Verve by Bright Voyaging
https://apps.example-store.com/au/app/sail-verve/id100000001

uRedlandTR by Travel Territory Board
https://apps.example-store.com/au/app/uredlandtr/id100000002

Wexmoor Trips
http://www.wexmoortrips.example.au

Trek Mapper by Voyage Bureau
http://apps.example-store.com/au/app/trek-mapper/id100000003

Sunward by Sunward Travel Office
https://apps.example-store.com/au/app/sunward/id100000004

Upper Fernridge Valley Route by Visit Coastlands
https://apps.example-store.com/au/app/upper-fernridge-valley-route/id100000005

Wanderer Path by Travel Territory Board and Southern Plains Travel Council
https://apps.example-store.com/au/app/wanderers-path-grand-journey/id100000006

Gordon Pellbrook Consulting (GPC)
November 2012 – Present (8 months)Brisbane, Sydney, Canberra

Gordon’s consults to Small-to-Medium Enterprises (SME) and Government organisations on business strategy, technology strategy, risk mitigation, disruptive technology and innovation in the workplace.

Gordon’s consultancy mantra is that we cannot divorce economic life from cultural life particularly in an era when social capital may be as important as physical capital in business.

Reason: request from designers, I want to see their best efforts

Target Market(s)

35+

Industry/Entity Type

Business

Requirements
Must have
• Please use some of the personal image(s) contained in the zip files which can be downloaded from here

http://filedrop.example/k9Xq2Lm
http://filedrop.example/p4Rt7Vn
http://filedrop.example/z8Hw3Bc
Nice to have
• Black, Sleek design, maybe minimalist. Nice to have a Pixelle for the design. Nice to have it easily ported to Wordpress or be a modified Wordpress template. HTML 5, responsive design

```html
<!DOCTYPE html>
<html lang="en">
<head>
<meta charset="utf-8">
<title>Gordon Pellbrook Consulting</title>
<link rel="stylesheet" href="https://fonts.googleapis.com/css2?family=Anton&family=Arimo:ital,wght@0,400;0,700;1,400;1,700&display=swap">
<style>
:root{
  --black:#000;
  --panel:#0c0c0c;
  --panel-edge:#141414;
  --gold:#a07712;
  --gold-bright:#c9981c;
  --gold-dark:#3a2a05;
  --circle:#272727;
  --box:#141414;
  --text:#fff;
  --muted:#bdbdbd;
  --link:#a9a9a9;
  --field:#2c2c2c;
  --rule:#2a2a2a;
}
*{margin:0;padding:0;box-sizing:border-box}
html,body{width:1200px;height:1000px;overflow:hidden;background:var(--black)}
body{position:relative;font-family:"Arimo",Arial,sans-serif;color:var(--text)}
.abs{position:absolute}
.page-panel{left:237px;top:0;width:756px;height:748px;background:linear-gradient(90deg,#080808,var(--panel-edge) 50%,#080808)}
.brand{left:308px;top:12px;font-weight:700;font-size:30px;letter-spacing:-.5px;color:var(--text);white-space:nowrap}
.hero{left:300px;top:65px;width:630px;height:211px;background:linear-gradient(90deg,#0a0802 0%,#5b430a 25%,#9c750f 55%,#7a5a0a 78%,#0b0803 100%)}
.hero-dots{left:315px;top:76px;display:flex;gap:5px}
.hero-dots span{width:9px;height:9px;border-radius:50%;background:#fff}
.hero-quote{left:320px;top:120px;width:425px;text-align:center;font-weight:700;text-transform:uppercase;letter-spacing:1.5px;font-size:16px;line-height:20px}
.hero-quote .big{font-size:27px;letter-spacing:1px}
.portrait{left:735px;top:30px;width:155px;height:246px;background:linear-gradient(180deg,#3a3836 0%,#1c1d24 35%,#111218 100%);border-radius:60px 60px 0 0}
.nav{left:300px;top:278px;width:630px;height:54px;display:flex}
.nav a{flex:1;display:flex;align-items:center;justify-content:center;color:var(--gold);text-decoration:none;font-size:13px;letter-spacing:1.5px;border-right:1px solid #1f1f1f;background:#0a0a0a;position:relative}
.nav a:last-child{border-right:0}
.nav a.current::after{content:"";position:absolute;left:0;right:0;bottom:0;height:5px;background:linear-gradient(90deg,#6d5108,var(--gold-bright),#6d5108)}
.feature{width:142px;height:142px;border-radius:50%;background:var(--circle);top:349px;box-shadow:0 0 12px #000;text-align:center}
.feature h2{font-family:"Anton",Impact,sans-serif;font-weight:400;font-size:27px;line-height:25px;margin-top:36px;letter-spacing:.3px}
.feature svg{margin-top:14px}
.sec-title{font-weight:700;font-size:15px;letter-spacing:.5px}
.testi-nav{left:554px;top:529px;color:var(--gold);font-size:18px;letter-spacing:8px}
.quote-box{left:322px;top:560px;width:271px;height:132px;background:var(--box)}
.quote-mark{left:335px;top:560px;font-size:44px;font-style:italic;font-weight:700;font-family:Georgia,serif}
.quote-text{left:336px;top:589px;width:246px;font-size:10.5px;line-height:12.5px;font-style:italic;color:var(--muted);text-align:justify;text-indent:46px}
.quote-author{left:420px;top:671px;width:161px;text-align:right;color:var(--gold);font-size:10.5px;font-weight:700;font-style:italic}
.more-link{font-size:12px;color:#bbb;letter-spacing:.5px;display:flex;align-items:center;gap:6px}
.more-link i{width:20px;height:18px;background:#777;display:flex;align-items:center;justify-content:center}
.divider{left:613px;top:508px;width:1px;height:240px;background:var(--rule)}
.news{left:640px;top:565px;width:280px;list-style:none;font-size:10.5px;line-height:12px}
.news li{display:flex;gap:7px;margin-bottom:5px}
.news li svg{flex:none;margin-top:2px}
.news a{color:var(--link)}
.foot-title{font-weight:700;font-size:13px;letter-spacing:.3px}
.foot-text{font-size:9.5px;line-height:10.5px;color:#d0d0d0}
.comments{left:512px;top:788px;width:197px;list-style:none;font-size:9px;color:#ccc}
.comments li{height:23.5px;border-bottom:1px solid var(--rule);display:flex;align-items:center;gap:6px}
.comments li::before{content:"";border-left:4px solid var(--gold);border-top:3px solid transparent;border-bottom:3px solid transparent;margin-left:2px}
.comments em{font-style:normal;color:var(--gold-bright)}
.field{left:738px;width:181px;background:var(--field);font-size:9px;color:#888;padding:4px 5px}
.submit{left:865px;top:910px;width:54px;height:19px;background:var(--gold);font-size:9px;display:flex;align-items:center;justify-content:center}
.copyright{left:237px;top:972px;width:756px;height:28px;background:#0b0b0b;font-size:8px;color:#555;text-align:center;line-height:30px}
</style>
</head>
<body>
<div class="abs page-panel"></div>

<div class="abs brand">Gordon Pellbrook Consulting</div>

<div class="abs hero"></div>
<div class="abs hero-dots"><span></span><span></span><span></span></div>
<div class="abs portrait" role="img" aria-label="Portrait photo of Gordon Pellbrook in a dark suit"></div>
<p class="abs hero-quote">“ We teach you how to <span class="big">Improve</span><br>your business processes,<br>and make the technology<br><span class="big">Affordable</span> for you. ”</p>

<nav class="abs nav">
  <a class="current" href="#">HOME</a><a href="#">ABOUT</a><a href="#">SERVICES</a><a href="#">WORKS</a><a href="#">BLOG</a><a href="#">CONTACT</a>
</nav>

<div class="abs feature" style="left:299px"><h2>LOREM<br>IPSUM 1</h2><svg width="28" height="28" viewBox="0 0 28 28"><circle cx="14" cy="14" r="12" fill="none" stroke="#a07712" stroke-width="2.4"/><path d="M7 14h12M14 8l6 6-6 6" fill="none" stroke="#a07712" stroke-width="2.6"/></svg></div>
<div class="abs feature" style="left:462px"><h2>LOREM<br>IPSUM 2</h2><svg width="28" height="28" viewBox="0 0 28 28"><circle cx="14" cy="14" r="12" fill="none" stroke="#a07712" stroke-width="2.4"/><path d="M7 14h12M14 8l6 6-6 6" fill="none" stroke="#a07712" stroke-width="2.6"/></svg></div>
<div class="abs feature" style="left:625px"><h2>LOREM<br>IPSUM 3</h2><svg width="28" height="28" viewBox="0 0 28 28"><circle cx="14" cy="14" r="12" fill="none" stroke="#a07712" stroke-width="2.4"/><path d="M7 14h12M14 8l6 6-6 6" fill="none" stroke="#a07712" stroke-width="2.6"/></svg></div>
<div class="abs feature" style="left:788px"><h2>LOREM<br>IPSUM 4</h2><svg width="28" height="28" viewBox="0 0 28 28"><circle cx="14" cy="14" r="12" fill="none" stroke="#a07712" stroke-width="2.4"/><path d="M7 14h12M14 8l6 6-6 6" fill="none" stroke="#a07712" stroke-width="2.6"/></svg></div>

<h3 class="abs sec-title" style="left:329px;top:531px">TESIMONIALS</h3>
<div class="abs testi-nav">&lt; &gt;</div>
<div class="abs quote-box"></div>
<div class="abs quote-mark">“</div>
<p class="abs quote-text">At vero eos et accusamus et iusto odio dignissimos ducimusqui blanditiis praesentvoluptatum deleniti atque quos dolores et quasmolestias excepturi occaecati cupide non provident, similique sunt in culpa qui...</p>
<p class="abs quote-author">Anonim Name | Company</p>
<div class="abs more-link" style="left:521px;top:706px">SEE ALL <i><svg width="12" height="10" viewBox="0 0 12 10"><path d="M1 5h9M6 1l4 4-4 4" fill="none" stroke="#fff" stroke-width="1.6"/></svg></i></div>

<div class="abs divider"></div>

<h3 class="abs sec-title" style="left:634px;top:531px">LATEST NEWS</h3>
<ul class="abs news">
  <li><svg width="11" height="9" viewBox="0 0 11 9"><path d="M0 4.5h9M5 1l4 3.5L5 8" fill="none" stroke="#aaa" stroke-width="1.4"/></svg><a href="#">Lorem Ipsum this is the title and it is a link</a></li>
  <li><svg width="11" height="9" viewBox="0 0 11 9"><path d="M0 4.5h9M5 1l4 3.5L5 8" fill="none" stroke="#aaa" stroke-width="1.4"/></svg><a href="#">Lorem Ipsum this is the title and it is a link and this is two lines, maximum is two lines</a></li>
  <li><svg width="11" height="9" viewBox="0 0 11 9"><path d="M0 4.5h9M5 1l4 3.5L5 8" fill="none" stroke="#aaa" stroke-width="1.4"/></svg><a href="#">Maximum is two line for the title</a></li>
  <li><svg width="11" height="9" viewBox="0 0 11 9"><path d="M0 4.5h9M5 1l4 3.5L5 8" fill="none" stroke="#aaa" stroke-width="1.4"/></svg><a href="#">Maximum is two line for the title</a></li>
  <li><svg width="11" height="9" viewBox="0 0 11 9"><path d="M0 4.5h9M5 1l4 3.5L5 8" fill="none" stroke="#aaa" stroke-width="1.4"/></svg><a href="#">Maximum is two line for the title</a></li>
  <li><svg width="11" height="9" viewBox="0 0 11 9"><path d="M0 4.5h9M5 1l4 3.5L5 8" fill="none" stroke="#aaa" stroke-width="1.4"/></svg><a href="#">Without any thumbnails</a></li>
</ul>
<div class="abs more-link" style="left:821px;top:706px">READ MORE <i><svg width="12" height="10" viewBox="0 0 12 10"><path d="M1 5h9M6 1l4 4-4 4" fill="none" stroke="#fff" stroke-width="1.6"/></svg></i></div>

<h4 class="abs foot-title" style="left:318px;top:764px">ABOUT US</h4>
<p class="abs foot-text" style="left:318px;top:790px;width:171px;text-align:justify">Lorem ipsum dolor sit amet consectetuer adipi scing elraesent ves tibm moeaean nummy hendrerit mauris.</p>
<p class="abs foot-text" style="left:318px;top:854px">4127 Kestrel Lane,<br>Dunmore, K17 3QT.<br>Freephone: &nbsp;+1 800 555 0142<br>FAX: &nbsp;+1 800 555 0187</p>

<h4 class="abs foot-title" style="left:513px;top:764px">RECENT COMMENTS</h4>
<ul class="abs comments">
  <li>There is a comment on blog 1 by <em>Anonimname</em></li>
  <li>There is a comment on blog 1 by <em>Anonimname</em></li>
  <li>There is a comment on blog 1 by <em>Anonimname</em></li>
  <li>There is a comment on blog 1 by <em>Anonimname</em></li>
</ul>

<h4 class="abs foot-title" style="left:737px;top:764px">CONTACT US</h4>
<div class="abs field" style="top:789px;height:18px">Name</div>
<div class="abs field" style="top:814px;height:18px">Email</div>
<div class="abs field" style="top:840px;height:65px">Message</div>
<div class="abs submit">SUBMIT</div>

<div class="abs copyright">© 2012 Gordon Pellbrook | All Rights Reserved</div>
</body>
</html>
```